i would like a business card to leave with customers and potential customers for electrical work and for the supply and install of reverse cycle airconditioning in the domestic and commercial market.
I own my own business and im a sole trader. I have an a'class electrical lisence and also a refrigeration lisence so i am
able to offer complete installations in airconditioning by a fully qualified and lisenced tradesman.
im looking for something that comes across as unique and professional.
i had the coluor black and some gold in mind but open to any coluors.
something like Beacon Electrical & Refrigeration
or Beacon Air.
i will use this design on a business card to advertise through summer to help generate installs through the busy season.

Target Market(s)

Mainly domestic house holds through summer who are in need of airconditioning and reliable information to acomadate thier cooling and heating requirements

Industry/Entity Type

Electrical

Requirements
Must have
• Business name- Beacon
My name- Peter Wollaston
My mobile no- 0457 819 302
My email- prwollaston@tarvel.com.au
Installation & Decomissioning of aiconditioning split systems
LIC NO: KTR 407516
Nice to have
• Beacon Electrical & Refrigeration

```html
<!DOCTYPE html>
<html lang="en">
<head>
<meta charset="utf-8">
<title>Beacon Electrical – Business Card</title>
<link href="https://fonts.googleapis.com/css2?family=Crimson+Pro:wght@400;500&display=swap" rel="stylesheet">
<style>
  :root {
    --backdrop: #3d4b4e;
    --card-dark: #1c1c1d;
    --card-mid: #2b2b2c;
    --brand-blue: #2a5caa;
    --band-blue: #2f78c4;
    --band-light: #4f9be0;
    --text-light: #e2e2e2;
    --text-muted: #8a8a8a;
    --badge: #f4f4f4;
  }
  * { margin: 0; padding: 0; box-sizing: border-box; }
  html, body { width: 1200px; height: 750px; overflow: hidden; }
  body {
    background: var(--backdrop);
    font-family: "Crimson Pro", Georgia, serif;
    position: relative;
  }
  .brand-lockup {
    position: absolute;
    display: flex;
    align-items: center;
    gap: 14px;
    color: var(--brand-blue);
    font-weight: 500;
    line-height: 1;
  }
  .brand-mark {
    display: block;
    background: var(--brand-blue);
  }
  .brand-lockup--hero { left: 620px; top: 92px; font-size: 78px; }
  .brand-lockup--hero .brand-mark { width: 96px; height: 96px; }

  .card {
    position: absolute;
    overflow: hidden;
    background: linear-gradient(160deg, var(--card-mid), var(--card-dark));
    box-shadow: 0 10px 24px rgba(0,0,0,.45);
  }
  .card--front { left: 52px; top: 160px; width: 500px; height: 310px; }
  .card--front .brand-lockup { left: 96px; top: 128px; font-size: 46px; gap: 10px; }
  .card--front .brand-mark { width: 56px; height: 56px; }

  .card--back { left: 617px; top: 335px; width: 543px; height: 330px; }
  .card--back .brand-lockup { left: 28px; top: 22px; font-size: 34px; gap: 8px; }
  .card--back .brand-mark { width: 44px; height: 44px; }

  .holder-name {
    position: absolute; right: 62px; top: 88px;
    font-size: 28px; color: var(--text-light); font-weight: 400;
  }
  .contact-list {
    position: absolute; left: 28px; top: 158px;
    list-style: none; font-size: 19px; line-height: 26px; color: var(--text-light);
  }
  .contact-list .label { color: var(--text-muted); margin-right: 6px; }
  .swoosh { position: absolute; left: 0; top: 0; width: 543px; height: 330px; }
  .service-line {
    position: absolute; left: 36px; top: 296px;
    font-size: 16px; color: var(--text-light);
  }
  .badge {
    position: absolute; left: 480px; top: 268px;
    width: 42px; height: 50px; background: var(--badge);
  }
</style>
</head>
<body>
  <div class="brand-lockup brand-lockup--hero">
    <span class="brand-mark"></span>
    <span class="brand-name">Beacon Electrical</span>
  </div>

  <section class="card card--front">
    <div class="brand-lockup">
      <span class="brand-mark"></span>
      <span class="brand-name">Beacon Electrical</span>
    </div>
  </section>

  <section class="card card--back">
    <svg class="swoosh" viewBox="0 0 543 330" aria-hidden="true">
      <path d="M0 258 C170 285 380 230 543 168 L543 330 L0 330 Z" fill="var(--band-light)"/>
      <path d="M0 268 C180 292 390 242 543 182 L543 330 L0 330 Z" fill="var(--band-blue)"/>
    </svg>
    <div class="brand-lockup">
      <span class="brand-mark"></span>
      <span class="brand-name">Beacon Electrical</span>
    </div>
    <h1 class="holder-name">Peter Wollaston</h1>
    <ul class="contact-list">
      <li><span class="label">mob:</span>0457 819 302</li>
      <li><span class="label">email:</span>prwollaston@tarvel.com.au</li>
      <li><span class="label">LIC No:</span>KTR 407516</li>
    </ul>
    <p class="service-line">Installation &amp; Decomissioning of airconditioning Split Systems</p>
    <span class="badge"></span>
  </section>
</body>
</html>
```